Classy business card for accounting firm

We're looking for a new business card for our accounting firm. Our logo was designed by Brandolith, so all of the design info we would like to use has been provided. The specific font provided isn't required to be used.

We want the card to look classy and elegent. Probably more minimalistic, but still with some pops of color.

The options we would like to include on the card are as follows:
1. Main office phone line
2. Direct phone line
3. Email address
4. Website URL
5. Name
6. Title (CEO, President, etc.)
7. Firm Address

The design and card should be double sided!!! The drop down box in the project brief for some reason is defaulting to single sided. Not sure why this is happening.

Thanks!

Contact Information for Business Card

The options we would like to include on the card are as follows: 1. Main office phone line 2. Direct phone line 3. Email address 4. Website URL 5. Name 6. Title (CEO, President, etc.) 7. Firm Address

Requirements
Must have
• Card must be double sided.

```html
<!DOCTYPE html>
<html lang="en">
<head>
<meta charset="utf-8">
<title>Ledgerline Associates – Business Card</title>
<link rel="stylesheet" href="https://fonts.googleapis.com/css2?family=Montserrat:wght@400;500;700&display=swap">
<style>
  :root {
    --backdrop: #1b1b1b;
    --card-white: #ffffff;
    --card-grey: #777777;
    --ink-grey: #666666;
    --brand-orange: #ff7f0a;
    --brand-green: #b5bd3a;
    --text-light: #ffffff;
  }
  * { box-sizing: border-box; margin: 0; padding: 0; }
  html, body {
    width: 1200px; height: 1189px; overflow: hidden;
    background: var(--backdrop);
    font-family: "Montserrat", Arial, sans-serif;
  }
  .sheet {
    width: 1200px; height: 1189px;
    display: flex; flex-direction: column; align-items: center; justify-content: center;
    gap: 60px;
  }
  .card {
    width: 700px; height: 400px; border-radius: 22px;
    position: relative; overflow: hidden;
  }
  /* front */
  .card--front { background: var(--card-white); display: flex; align-items: center; padding: 0 50px 0 60px; }
  .front-brand { width: 220px; flex-shrink: 0; display: flex; flex-direction: column; align-items: center; gap: 18px; }
  .brand-square { width: 84px; height: 84px; background: var(--brand-orange); }
  .front-brand .brand-name {
    color: var(--brand-orange); font-weight: 700; font-size: 19px; letter-spacing: 2px;
  }
  .divider { width: 2px; height: 200px; flex-shrink: 0; background: var(--brand-orange); margin: 0 38px 0 30px; }
  .contact { color: var(--ink-grey); }
  .contact .person-name { font-weight: 700; font-size: 28px; letter-spacing: 1.5px; text-transform: uppercase; line-height: 1.15; }
  .contact .person-title { font-weight: 400; font-size: 19px; margin: 2px 0 8px; }
  .contact p { font-size: 15px; line-height: 1.45; letter-spacing: 0.4px; }
  .contact .label { font-weight: 700; }
  /* back */
  .card--back {
    background: var(--card-grey);
    display: flex; flex-direction: column; align-items: center; justify-content: center;
  }
  .back-square { width: 64px; height: 64px; background: var(--brand-orange); margin-bottom: 26px; }
  .back-name {
    color: var(--text-light); font-weight: 500; font-size: 40px; letter-spacing: 3px; text-transform: uppercase;
  }
  .tagline-row { display: flex; align-items: center; gap: 16px; margin-top: 10px; }
  .tagline-rule { width: 100px; height: 2px; background: var(--brand-green); }
  .tagline { color: var(--text-light); font-weight: 500; font-size: 17px; letter-spacing: 3px; text-transform: uppercase; }
</style>
</head>
<body>
<main class="sheet">
  <section class="card card--front" aria-label="Card front">
    <div class="front-brand">
      <span class="brand-square" aria-hidden="true"></span>
      <span class="brand-name">LEDGERLINE</span>
    </div>
    <span class="divider" aria-hidden="true"></span>
    <div class="contact">
      <h1 class="person-name">Daniel Brooks</h1>
      <h2 class="person-title">CEO/President</h2>
      <p>Your Address, City<br>State, Country, Zip 12356</p>
      <p><span class="label">P</span>. (555) 014-2870 (Main)</p>
      <p><span class="label">P</span>. (555) 019-3461 (Direct)</p>
      <p><span class="label">E</span>. info@ledgerlineassociates.com</p>
      <p><span class="label">W</span>. ledgerlineassociates.com</p>
    </div>
  </section>

  <section class="card card--back" aria-label="Card back">
    <span class="back-square" aria-hidden="true"></span>
    <div class="back-name">Ledgerline Associates</div>
    <div class="tagline-row">
      <span class="tagline-rule" aria-hidden="true"></span>
      <span class="tagline">Solving Tax Problems</span>
      <span class="tagline-rule" aria-hidden="true"></span>
    </div>
  </section>
</main>
</body>
</html>
```